Artwork-Design (Cover) für Musikalbum
Zielgruppe
Wir sind eine Tonträgerfirma und bewegen uns im Low-Budget-Segment.
Aufgabenstellung
Artwork-Design (Cover) für ein Musikalbum : 'Songs From The Prairie'
Wir benötigen nicht das komplette Artwork, sondern ein Frontcover
(121 x 120 mm + 20 mm Beschnitt) wg. etwaiger Verschiebung der Positionierung.
Fertigstellung (Aufziehen des Inlays und Labels) erfolgt später bei uns im Hause.
Wir benötigen später eine offene psd-Datei mit allen Ebenen.
Wichtig: Schriften nicht gerastert ggfs. Schrift mitliefern.
Was wir uns vorstellen:
- Entsprechend der Musik Bild, Tracks Beispiele:
-HALF A MOONLIGHT - TALWIND
-FARMYARD LADY IN A GREY MOOD - MERRIT, ODESSA P
-MAGGIE PLEASE COME BACK TO THE HOLLOW - BAXLEY, ORVAL
-PORTRAIT OF A DRIFTER - HOLTZ, WADE
- Bildmaterial sollte bei bildwerkpool, lumarchiv oder p-depot ausgesucht werden, das Bildmaterial wird dann später auch von uns dort eingekauft.
- keine Künstlerfotos.
Wir freuen uns und sind sehr gespannt auf eure Vorschläge,
bei Fragen gerne mailen

```html
<!DOCTYPE html>
<html lang="en">
<head>
<meta charset="utf-8">
<title>Songs From The Prairie – Album Cover</title>
<link rel="stylesheet" href="https://fonts.googleapis.com/css2?family=Roboto+Slab:wght@300;400;500&display=swap">
<style>
  :root {
    --page-bg: #ffffff;
    --wood-deep: #5a2e14;
    --wood-mid: #b8682a;
    --wood-light: #e3a55a;
    --shade-dark: #2f2a22;
    --shade-muted: #7a7a66;
    --shirt-pale: #c9bfa4;
    --frame-line: rgba(255, 240, 205, 0.85);
    --badge-fill: rgba(247, 226, 140, 0.88);
    --badge-halo: rgba(255, 252, 235, 0.92);
    --badge-ring: #7a3d25;
    --title-ink: #7a3d25;
    --track-ink: #fff6e6;
  }

  * { box-sizing: border-box; margin: 0; padding: 0; }

  html, body {
    width: 1200px;
    height: 1200px;
    overflow: hidden;
    background: var(--page-bg);
  }

  .album-cover {
    position: relative;
    width: 1200px;
    height: 1200px;
    overflow: hidden;
    font-family: "Roboto Slab", Georgia, serif;
  }

  .cover-photo {
    position: absolute;
    inset: 0;
    background:
      radial-gradient(ellipse 38% 55% at 34% 55%, rgba(233, 160, 80, 0.85), rgba(233, 160, 80, 0) 70%),
      radial-gradient(ellipse 30% 40% at 80% 30%, rgba(201, 191, 164, 0.9), rgba(201, 191, 164, 0) 75%),
      radial-gradient(ellipse 25% 35% at 90% 75%, rgba(47, 42, 34, 0.85), rgba(47, 42, 34, 0) 80%),
      linear-gradient(100deg, var(--wood-deep) 0%, var(--wood-mid) 22%, var(--wood-light) 42%, var(--wood-mid) 60%, var(--shade-muted) 78%, var(--shade-dark) 100%);
  }

  .cover-frame {
    position: absolute;
    inset: 20px;
    border: 4px solid var(--frame-line);
  }

  .title-badge {
    position: absolute;
    left: 50%;
    top: 50%;
    width: 612px;
    height: 612px;
    transform: translate(-50%, -50%);
    border-radius: 50%;
    background: var(--badge-fill);
    box-shadow: 0 0 0 6px var(--badge-halo);
    display: flex;
    align-items: center;
    justify-content: center;
  }

  .title-badge::before {
    content: "";
    position: absolute;
    inset: 14px;
    border-radius: 50%;
    border: 4px solid var(--badge-ring);
  }

  .album-title {
    position: relative;
    text-align: center;
    color: var(--title-ink);
    font-weight: 400;
    text-transform: uppercase;
    line-height: 0.9;
    letter-spacing: -1px;
  }

  .album-title .title-line { display: block; }
  .album-title .title-line--top { font-size: 118px; }
  .album-title .title-line--middle { font-size: 82px; font-weight: 300; }
  .album-title .title-line--bottom { font-size: 100px; }

  .track-list {
    position: absolute;
    left: 0;
    right: 0;
    top: 1002px;
    list-style: none;
    text-align: center;
    color: var(--track-ink);
    font-size: 21px;
    font-weight: 300;
    line-height: 31px;
    text-transform: uppercase;
    text-shadow: 0 1px 2px rgba(60, 30, 10, 0.35);
  }
</style>
</head>
<body>
  <main class="album-cover">
    <div class="cover-photo" role="img" aria-label="Close-up photograph of an acoustic guitar being played, warm sepia and amber tones"></div>
    <div class="cover-frame"></div>

    <div class="title-badge">
      <h1 class="album-title">
        <span class="title-line title-line--top">Songs</span>
        <span class="title-line title-line--middle">From The</span>
        <span class="title-line title-line--bottom">Prairie</span>
      </h1>
    </div>

    <ul class="track-list">
      <li>• Half a Moonlight - Talwind • Farmyard Lady in a Grey Mood - Merrit, Odessa P</li>
      <li>• Maggie Please Come Back to the Hollow - Baxley, Orval</li>
      <li>• Portrait of a Drifter - Holtz, Wade</li>
    </ul>
  </main>
</body>
</html>
```